6' Banner Stands for exhibiting to Health Fairs with an audience of age 55+

We need designs for two 6' banner stands to stand on either side of our exhibition tables. We offer Hereditary Cancer Screening. I want the banners to have the same look and feel as the logo and the files color scheme logo, etc..

The Banners should have "Hereditary Cancer Screening" at the top with the Tag Line "The Test You Take For Them" underneath. A photo of grandparents with kids/grandkids and underneath the photos in large font one of the following messages:
1) "A Simple Swab Could Save A Family Members LIFE Get Tested Today!"
2) "Does Cancer Run In Your Family? Get Tested Today!"
3) "Knowledge Is Power" "Get Tested Today!"
4) "Will You Give Your Loved Ones The Information To Beat Cancer In Their Lives? Get Tested Today!
5) Knowledge Is Power Get Tested Today!"
Updates

Thank you all for your designs I now have the exact specs for the banners, so please use these as you update your designs. 31.5 inches X 83.25 inches and add a 1/2 inch bleed to all 4 sides. Thank you.

Target Market(s)

Persons 55+ who are grandparents

Industry/Entity Type

Healthcare

Font styles to use
Sans Serif
Other font styles liked:
• Comic Sans for "The Test You Take For Them"

Colors
9bcb3c
0356a4
ffffff

Requirements
Must have
• the main focus should be the hereditary cancer screening; "Hereditary Cancer Screening";
• "The test you order for them" in Comic Sans font underneath
• A photo or photos of grandparents with their grandchildren (multiple ethnicities)
• One of the slogans listed above
• GET TESTED TODAY underneath the messages at the bottom of the banner highlighted and eye catching
• www.kinhealthcheckup.net
Nice to have
• Logo at the top or bottom

```html
<!DOCTYPE html>
<html lang="en">
<head>
<meta charset="utf-8">
<title>Hereditary Cancer Screening – Banner Stands</title>
<link rel="stylesheet" href="https://fonts.googleapis.com/css2?family=Comic+Neue:wght@400;700&family=Noto+Serif:wght@700&family=Oswald:wght@500;600&display=swap">
<style>
  :root {
    --navy: #24264f;
    --green: #8dc63f;
    --white: #ffffff;
    --stage: #a9a9a9;
    --label: #1e1e1e;
    --ink: #111111;
  }
  * { box-sizing: border-box; margin: 0; padding: 0; }
  html, body { width: 1200px; height: 703px; overflow: hidden; }
  body { background: var(--stage); position: relative; font-family: "Comic Neue", sans-serif; }

  .banner-label { position: absolute; font: 400 9px/1 "Oswald", sans-serif; letter-spacing: .5px; color: var(--label); }

  .banner { position: absolute; width: 262px; height: 604px; background: var(--white); overflow: hidden; }
  .banner > * { position: absolute; }
  .bar-green { left: 0; top: 0; width: 203px; height: 11px; background: var(--green); }
  .bar-navy { left: 208px; top: 0; width: 54px; height: 11px; background: var(--navy); }

  .title { left: 0; width: 100%; text-align: center; font: 700 23px/21px "Noto Serif", serif; color: var(--navy); }
  .tagline { left: 0; width: 100%; text-align: center; font: 400 14.5px/1 "Comic Neue", sans-serif; color: var(--green); }

  .photo-warm { background: linear-gradient(135deg, #cfcdb6 0%, #d8c4b3 55%, #c6c9c4 100%); }
  .photo-sun  { background: linear-gradient(160deg, #b9c29a 0%, #dccab9 55%, #d9bcbc 100%); }
  .photo-soft { background: linear-gradient(140deg, #cdb7a1 0%, #e0cfc1 60%, #c9c8c6 100%); }
  .photo-grey { background: linear-gradient(140deg, #8e8e8e 0%, #bdbdbd 60%, #9c9c9c 100%); }

  .panel { background: var(--navy); color: var(--white); }
  .accent { color: var(--green); font-weight: 700; }

  .cta { left: 0; width: 100%; text-align: center; font: 400 18px/1 "Comic Neue", sans-serif; color: var(--navy); }
  .cta .accent { font-size: 25px; }

  .brand { left: 0; width: 100%; display: flex; justify-content: center; align-items: center; gap: 8px; }
  .brand-dot { width: 40px; height: 40px; border-radius: 50%; background: var(--navy); flex: none; }
  .brand-name { font: 700 16px/15px "Comic Neue", sans-serif; color: var(--navy); text-transform: uppercase; letter-spacing: .5px; }

  .footer { left: 0; bottom: 0; width: 100%; height: 44px; background: var(--navy); display: flex; align-items: center; justify-content: center; }
  .url { font: 400 17px/1 "Comic Neue", sans-serif; color: var(--green); }

  /* Banner 1 */
  .question { left: 0; top: 402px; width: 100%; height: 60px; display: flex; align-items: center; justify-content: center; text-align: center; font: 400 19px/24px "Comic Neue", sans-serif; }
  .question .accent { font-size: 21px; }

  /* Banner 2 */
  .swab { left: 0; top: 159px; width: 112px; height: 167px; padding: 18px 0 0 19px; font: 400 19px/20px "Comic Neue", sans-serif; }
  .swab .accent { font-size: 22px; }

  /* Banner 3 */
  .headline { left: 0; width: 100%; text-align: center; font-family: "Oswald", sans-serif; font-weight: 600; color: var(--ink); text-transform: uppercase; }
  .headline-give { top: 276px; font-size: 32px; line-height: 44px; letter-spacing: -.5px; }
  .headline-give .big { font-size: 48px; color: var(--navy); }
  .headline-loved { top: 318px; font-size: 32px; line-height: 34px; letter-spacing: -.5px; }
  .headline-band { left: 26px; top: 352px; width: 213px; height: 28px; background: var(--navy); color: var(--white); font: 500 20px/28px "Oswald", sans-serif; text-align: center; text-transform: uppercase; }
  .headline-cancer { top: 380px; font-size: 66px; line-height: 74px; color: var(--green); letter-spacing: 1px; }
  .headline-lives { top: 450px; font-size: 34px; line-height: 40px; letter-spacing: -.5px; }

  /* Banner 4 */
  .knowledge { left: 0; top: 290px; width: 100%; height: 136px; }
  .knowledge-lead { position: absolute; left: 12px; top: 10px; width: 240px; font: 400 22px/27px "Comic Neue", sans-serif; }
  .knowledge-lead .line-2 { display: block; text-align: right; }
  .knowledge-bulb { position: absolute; left: 18px; top: 62px; }
  .knowledge-power { position: absolute; left: 104px; top: 74px; font: 400 22px/26px "Comic Neue", sans-serif; color: var(--green); }
  .knowledge-power .line-2 { display: block; padding-left: 26px; font-size: 28px; line-height: 30px; }
</style>
</head>
<body>

  <span class="banner-label" style="left:42px;top:44px">BANNER 1</span>
  <span class="banner-label" style="left:327px;top:46px">BANNER 2</span>
  <span class="banner-label" style="left:609px;top:43px">BANNER 3</span>
  <span class="banner-label" style="left:889px;top:43px">BANNER 4</span>

  <section class="banner" style="left:42px;top:64px">
    <div class="bar-green"></div><div class="bar-navy"></div>
    <h1 class="title" style="top:40px">Hereditary<br>Cancer Screening</h1>
    <p class="tagline" style="top:101px">The Test You Take For Them</p>
    <div class="photo-warm" style="left:0;top:134px;width:262px;height:162px" role="img" aria-label="Photo of three generations of a family standing together outdoors"></div>
    <div class="photo-sun" style="left:0;top:302px;width:126px;height:100px" role="img" aria-label="Photo of grandparents playing with a baby on the grass"></div>
    <div class="photo-grey" style="left:132px;top:302px;width:130px;height:100px" role="img" aria-label="Photo of a grandmother hugging her granddaughter"></div>
    <div class="panel question"><p>DOES <span class="accent">CANCER</span> Run in<br>Your <span class="accent">Family?</span></p></div>
    <p class="cta" style="top:470px">Get Tested <span class="accent">TODAY!</span></p>
    <div class="brand" style="top:506px;height:44px"><span class="brand-dot"></span><span class="brand-name">Kinward<br>Health<br>Group</span></div>
    <footer class="footer"><span class="url">www.kinhealthcheckup.net</span></footer>
  </section>

  <section class="banner" style="left:324px;top:61px">
    <div class="bar-green"></div><div class="bar-navy"></div>
    <h1 class="title" style="top:44px">Hereditary<br>Cancer Screening</h1>
    <p class="tagline" style="top:106px">The Test You Take For Them</p>
    <div class="panel swab">A Simple<br><span class="accent">Swab</span><br>Could<br><span class="accent">SAVE</span> A<br>Family<br>Members<br><span class="accent">LIFE</span></div>
    <div class="brand" style="left:112px;width:150px;top:164px;height:44px"><span class="brand-dot"></span><span class="brand-name">Kinward<br>Health<br>Group</span></div>
    <div class="photo-soft" style="left:120px;top:230px;width:142px;height:96px" role="img" aria-label="Photo of a grandfather cheek to cheek with his grandson"></div>
    <div class="photo-sun" style="left:0;top:331px;width:262px;height:216px" role="img" aria-label="Photo of smiling grandparents with their two grandchildren in a garden"></div>
    <footer class="footer"><span class="url">www.kinhealthcheckup.net</span></footer>
  </section>

  <section class="banner" style="left:609px;top:60px">
    <div class="bar-green"></div><div class="bar-navy"></div>
    <h1 class="title" style="top:28px">Hereditary<br>Cancer Screening</h1>
    <div class="photo-sun" style="left:0;top:92px;width:262px;height:184px" role="img" aria-label="Photo of grandparents laughing with their grandchildren"></div>
    <p class="headline headline-give">Will you <span class="big">Give</span></p>
    <p class="headline headline-loved">Your loved ones</p>
    <p class="headline-band">The information to beat</p>
    <p class="headline headline-cancer">Cancer</p>
    <p class="headline headline-lives">In their lives ?</p>
    <div class="brand" style="top:500px;height:46px"><span class="brand-dot"></span><span class="brand-name">Kinward<br>Health<br>Group</span></div>
    <footer class="footer"><span class="url">www.kinhealthcheckup.net</span></footer>
  </section>

  <section class="banner" style="left:889px;top:60px">
    <div class="bar-green"></div><div class="bar-navy"></div>
    <h1 class="title" style="top:40px">Hereditary<br>Cancer Screening</h1>
    <p class="tagline" style="top:102px">The Test You Take For Them</p>
    <div class="photo-soft" style="left:0;top:130px;width:122px;height:154px" role="img" aria-label="Photo of a grandmother embracing her granddaughter"></div>
    <div class="photo-warm" style="left:126px;top:130px;width:136px;height:154px" role="img" aria-label="Photo of a smiling multi-generation family group"></div>
    <div class="panel knowledge">
      <p class="knowledge-lead">knowing is better than <span class="line-2">not knowing.</span></p>
      <svg class="knowledge-bulb" width="70" height="60" viewBox="0 0 70 60" aria-hidden="true">
        <g fill="none" stroke="#8dc63f" stroke-width="2.5" stroke-linecap="round">
          <path d="M35 12c-10 0-16 7-16 15 0 6 4 9 7 13v5h18v-5c3-4 7-7 7-13 0-8-6-15-16-15z"/>
          <path d="M28 50h14M30 55h10"/>
          <path d="M35 2v5M12 10l4 4M58 10l-4 4M4 27h6M60 27h6M12 44l4-3M58 44l-4-3"/>
        </g>
      </svg>
      <p class="knowledge-power">Knowledge <span class="line-2">is Power</span></p>
    </div>
    <p class="cta" style="top:447px">Get Tested <span class="accent">TODAY!</span></p>
    <div class="brand" style="top:490px;height:46px"><span class="brand-dot"></span><span class="brand-name">Kinward<br>Health<br>Group</span></div>
    <footer class="footer"><span class="url">www.kinhealthcheckup.net</span></footer>
  </section>

</body>
</html>
```